Powerpoint design template for PLAYNOVA for new digital platform

We would like to use a PowerPoint template, we would like to create a new page, we would like to create a new digital platform PLAYNOVA for schools and parents for the creation of playful communication and educational tools for children to enhance their positive development, amaze them learn in a playful way. This platform is going to be the most creative, stimulating and innovative classroom, easy to use and fast to implement. Scrapbooking, collages ... Magazine, newsletters Diplomla / awards Slideshows Facebook Calendars Organizers Greetings Games ... This powerpoint template will be used essential to We are looking for a professional design, positioning our brand in the children market with an adult hearing. so you will need to find a good deal. Primary target: nurseries & schools from 0 to 18 years old and universities (in 2nd phase) Secondary target: small & medium businesses Third target: general public, and TPE If it is a color scheme, then it is suggested that it be marketed in Europe (UK, Italy, Spain) and in a 2nd Stage USA and other countries. multiple options for front page, insidious pages (multiple styles with limited text and extended text) and final contact page We need something to read, we can not do it too much, but we can not do it. , and inside pages aligned to our logo

Target Market(s)

Target 1; Education with teacher Target 2; parents and grandparents

Industry/Entity Type

Education

Font styles to use
Other font styles liked:
• not decided. but not too fancy

Requirements
Must have
• Multi page options for front page, page insides (multiple styles with limited text and extended text) and final page contact
Nice to have
• do not have a lot of ideas. We need something to read, we can not get away from it
Should not have
• not too fancy and busy: keep clarity & simplicity while reassuring on quality

```html
<!DOCTYPE html>
<html lang="en">
<head>
<meta charset="utf-8">
<title>PLAYNOVA – Presentation Template Overview</title>
<link href="https://fonts.googleapis.com/css2?family=Roboto:wght@300;400;500;700;900&display=swap" rel="stylesheet">
<style>
  :root{
    --bg:#404040;
    --white:#ffffff;
    --lime:#dbe24e;
    --lime-light:#c8d93c;
    --green:#8dc63f;
    --green-dark:#6fae2c;
    --sky:#13bdec;
    --cyan:#3ec3e8;
    --ink:#2e3440;
    --grey:#8a8f96;
    --rule:#e4ecc0;
    --chart-bg:#3a3f45;
    --orange:#e8862a;
  }
  *{box-sizing:border-box;margin:0;padding:0}
  html,body{width:1200px;height:1200px;overflow:hidden;background:var(--bg)}
  body{font-family:"Roboto",Arial,sans-serif;color:var(--ink);position:relative}
  .slide{position:absolute;background:var(--white);overflow:hidden;box-shadow:0 2px 6px rgba(0,0,0,.35)}
  .slide--large{width:566px;height:318px}
  .slide--small{width:270px;height:152px}
  .abs{position:absolute}
  .fill{position:absolute}

  /* brand wordmark */
  .wordmark{display:flex;align-items:center;gap:6px}
  .wordmark__square{background:var(--green);flex:none}
  .wordmark__name{font-weight:900;color:var(--ink);letter-spacing:.02em}
  .tagline{font-weight:400;letter-spacing:.28em;color:var(--ink);text-transform:uppercase}

  .cover-title{position:absolute;color:var(--white);font-weight:700;text-align:center;font-size:36px;line-height:42px}

  /* footer of content slides */
  .foot{position:absolute;left:6px;right:20px;bottom:8px;display:flex;align-items:center;gap:6px}
  .foot__mark{font-size:5px;font-weight:900;color:var(--ink);display:flex;align-items:center;gap:2px}
  .foot__mark i{display:block;width:5px;height:5px;background:var(--green)}
  .foot__rule{flex:1;height:1px;background:var(--rule)}

  .s-title{font-size:9px;font-weight:700;color:var(--ink)}
  .s-sub{font-size:8.5px;font-weight:300;color:var(--ink)}
  .tiny{font-size:4.6px;line-height:6.4px;color:var(--grey)}
  .tiny-list{list-style:none}
  .tiny-list li{position:relative;padding-left:5px;margin-bottom:2.6px}
  .tiny-list li::before{content:"•";position:absolute;left:0}

  .bubble{position:absolute;background:var(--green);color:var(--white);font-size:4.4px;font-weight:700;font-style:italic;line-height:5.6px;padding:4px 4px}
  .bubble::after{content:"";position:absolute;left:50%;bottom:-5px;margin-left:-5px;border:5px solid transparent;border-bottom:0;border-top-color:var(--green)}

  .icon-card{position:absolute;top:28px;width:60px}
  .icon-card__box{width:60px;height:52px;background:#eef1f3;display:flex;align-items:center;justify-content:center;
    background-image:linear-gradient(#e3e7ea 1px,transparent 1px),linear-gradient(90deg,#e3e7ea 1px,transparent 1px);background-size:5px 5px}
  .icon-card__title{font-size:4.8px;font-weight:700;margin-top:8px}
  .icon-card__text{font-size:4.4px;line-height:5.6px;color:var(--grey);margin-top:2px}

  .overlay-title{position:absolute;color:var(--white);font-size:7.5px;font-weight:700;text-align:center;width:86px}
  .overlay-text{position:absolute;color:rgba(255,255,255,.85);font-size:4px;line-height:5px;text-align:center;width:86px}

  .sheet-label{position:absolute;font-size:4.5px;color:var(--ink)}

  .magnifier{position:absolute;border-radius:50%;background:var(--white);box-shadow:0 2px 8px rgba(0,0,0,.35);overflow:hidden}

  /* feature copy */
  .feature{position:absolute;top:878px;color:var(--white)}
  .feature__head{font-size:27.5px;font-weight:700;line-height:34px;text-transform:uppercase;letter-spacing:.005em}
  .feature__body{font-size:28.5px;font-weight:300;line-height:34.5px}
</style>
</head>
<body>

<!-- Cover A: lime -->
<section class="slide slide--large" style="left:31px;top:31px">
  <svg class="fill" width="566" height="318" viewBox="0 0 566 318">
    <polygon points="219,0 566,0 566,318 300,142 " fill="#b9cf36"/>
    <polygon points="229,0 566,0 566,318 306,142" fill="var(--lime-light)"/>
    <polygon points="239,0 566,0 566,318 324,318 283,247 311,142" fill="var(--lime)"/>
  </svg>
  <div class="abs" style="left:44px;top:132px">
    <div class="wordmark"><span class="wordmark__square" style="width:16px;height:16px"></span><span class="wordmark__name" style="font-size:30px">PLAYNOVA</span></div>
    <div class="tagline" style="font-size:10px;line-height:12px;margin-top:14px;margin-left:4px">Your tagline<br>goes here</div>
  </div>
  <h1 class="cover-title" style="left:346px;top:106px;width:170px">Platform<br>for Kids</h1>
</section>

<!-- Cover B: sky -->
<section class="slide slide--large" style="left:31px;top:364px;background:var(--sky)">
  <h1 class="cover-title" style="left:74px;top:95px;width:170px">Platform<br>for kids</h1>
  <svg class="fill" width="566" height="318" viewBox="0 0 566 318">
    <g fill="var(--white)">
      <circle cx="300" cy="265" r="56"/>
      <circle cx="370" cy="215" r="58"/>
      <circle cx="450" cy="180" r="55"/>
      <circle cx="520" cy="165" r="50"/>
      <circle cx="560" cy="150" r="40"/>
      <rect x="300" y="210" width="266" height="108"/>
      <rect x="244" y="265" width="60" height="53"/>
    </g>
  </svg>
  <div class="abs" style="left:372px;top:242px">
    <div class="wordmark"><span class="wordmark__square" style="width:12px;height:12px"></span><span class="wordmark__name" style="font-size:23px">PLAYNOVA</span></div>
    <div class="tagline" style="font-size:7.5px;line-height:9px;margin-top:8px;margin-left:2px">Your tagline<br>goes here</div>
  </div>
</section>

<!-- Bullets slide -->
<section class="slide slide--small" style="left:612px;top:31px">
  <div class="abs" style="left:6px;top:6px">
    <div class="s-title">Super title</div>
    <div class="s-sub">Cool subtitle</div>
  </div>
  <ul class="tiny-list tiny abs" style="left:12px;top:31px;width:175px">
    <li>Far away, beyond the tall hills, lives a quiet village of words and letters.</li>
    <li>They gather each morning near the river, sharing stories and small ideas with friends.</li>
    <li>It is a bright place where every sentence finds a home and every word is heard.</li>
    <li>One day a short line of text decided to travel far.</li>
  </ul>
  <div class="foot"><span class="foot__mark"><i></i>PLAYNOVA</span><span class="foot__rule"></span></div>
</section>

<!-- Chart slide -->
<section class="slide slide--small" style="left:898px;top:31px">
  <div class="abs" style="left:6px;top:6px">
    <div class="s-title">Super title</div>
    <div class="s-sub">Cool subtitle</div>
  </div>
  <svg class="abs" style="left:6px;top:34px" width="124" height="85" viewBox="0 0 124 85">
    <rect width="124" height="85" fill="var(--chart-bg)"/>
    <text x="62" y="8" fill="#fff" font-size="5.5" font-weight="700" text-anchor="middle" font-family="Roboto, sans-serif">Chart Title</text>
    <g stroke="#50565c" stroke-width=".4">
      <line x1="10" y1="16" x2="118" y2="16"/><line x1="10" y1="28" x2="118" y2="28"/>
      <line x1="10" y1="40" x2="118" y2="40"/><line x1="10" y1="52" x2="118" y2="52"/>
      <line x1="10" y1="64" x2="118" y2="64"/>
    </g>
    <g fill="var(--green)">
      <rect x="14" y="38" width="4" height="26"/><rect x="19" y="50" width="4" height="14" fill="#c6de5a"/><rect x="24" y="52" width="4" height="12" fill="#a9cf3c"/>
      <rect x="40" y="26" width="4" height="38"/><rect x="45" y="50" width="4" height="14" fill="#c6de5a"/><rect x="50" y="34" width="4" height="30" fill="#a9cf3c"/>
      <rect x="66" y="44" width="4" height="20"/><rect x="71" y="36" width="4" height="28" fill="#c6de5a"/><rect x="76" y="40" width="4" height="24" fill="#a9cf3c"/>
      <rect x="92" y="50" width="4" height="14"/><rect x="97" y="32" width="4" height="32" fill="#c6de5a"/><rect x="102" y="22" width="4" height="42" fill="#a9cf3c"/>
    </g>
    <g fill="#aab" font-size="3" font-family="Roboto, sans-serif" text-anchor="middle">
      <text x="21" y="70">Category 1</text><text x="47" y="70">Category 2</text><text x="73" y="70">Category 3</text><text x="99" y="70">Category 4</text>
      <text x="62" y="77">● Series 1  ● Series 2  ● Series 3</text>
    </g>
  </svg>
  <p class="tiny abs" style="left:135px;top:33px;width:128px;font-size:4.4px;line-height:5.9px">Far away, beyond the tall hills, there lives a quiet village of words. They rest by the river and share small stories each day. A gentle stream runs past their homes and brings them new ideas. It is a bright land where sentences grow freely. Even the busiest words stop to listen here. One day a short line of text left home to explore the wide world of grammar and came back with many tales.</p>
  <div class="foot"><span class="foot__mark"><i></i>PLAYNOVA</span><span class="foot__rule"></span></div>
</section>

<!-- Photo trio slide -->
<section class="slide slide--small" style="left:612px;top:197px">
  <div class="bubble" style="left:6px;top:6px;width:84px;height:37px">Yes, I do have important things to say for far away, behind the word hills, far from the towns of Letters and Sounds.</div>
  <div class="bubble" style="left:93px;top:6px;width:84px;height:37px">Yes, I do have important things to say for far away, behind the word hills, far from the towns of Letters and Sounds.</div>
  <div class="bubble" style="left:181px;top:6px;width:84px;height:37px">Yes, I do have important things to say for far away, behind the word hills, far from the towns of Letters and Sounds.</div>
  <div class="fill" role="img" aria-label="Photo of a young child playing outdoors" style="left:6px;top:48px;width:84px;height:70px;background:linear-gradient(180deg,#a8c6dc,#c7b9a8 60%,#d44 100%)"></div>
  <div class="fill" role="img" aria-label="Photo of a girl studying at a desk" style="left:93px;top:48px;width:84px;height:70px;background:linear-gradient(135deg,#3c3028,#8a7a6c 60%,#e9e6e2)"></div>
  <div class="fill" role="img" aria-label="Photo of a smiling boy at a summer celebration" style="left:181px;top:48px;width:84px;height:70px;background:linear-gradient(160deg,#4fa8c8,#8c5a3c 55%,#c4474a)"></div>
  <div class="foot"><span class="foot__mark"><i></i>PLAYNOVA</span><span class="foot__rule"></span></div>
</section>

<!-- Charts slide -->
<section class="slide slide--small" style="left:898px;top:197px">
  <svg class="fill" width="270" height="152" viewBox="0 0 270 152">
    <g font-family="Roboto, sans-serif" font-size="5" fill="#555" text-anchor="middle">
      <text x="49" y="40">Chart Title</text><text x="135" y="40">Sales</text><text x="221" y="40">Chart Title</text>
    </g>
    <g stroke="#fff" stroke-width="1">
      <rect x="13" y="44" width="36" height="32" fill="var(--green)"/>
      <rect x="49" y="44" width="24" height="20" fill="#b6d84a"/>
      <rect x="73" y="44" width="12" height="20" fill="#c9e05e"/>
      <rect x="49" y="64" width="36" height="12" fill="#9fcd3a"/>
      <rect x="13" y="76" width="18" height="28" fill="#c9e05e"/>
      <rect x="31" y="76" width="26" height="28" fill="var(--green)"/>
      <rect x="57" y="76" width="28" height="28" fill="#b6d84a"/>
    </g>
    <circle cx="135" cy="73" r="23" fill="none" stroke="var(--sky)" stroke-width="7"/>
    <path d="M135 50 A23 23 0 0 1 152 58" fill="none" stroke="#7ed6f2" stroke-width="7"/>
    <g fill="none" stroke="#ddd" stroke-width=".5">
      <polygon points="221,46 248,64 238,96 204,96 194,64"/>
      <polygon points="221,58 237,68 231,86 211,86 205,68"/>
    </g>
    <polygon points="221,52 246,66 232,92 206,80 200,66" fill="var(--orange)"/>
    <polygon points="221,60 234,72 226,88 210,84 206,70" fill="#f6c89a"/>
    <g font-family="Roboto, sans-serif" font-size="3" fill="#999" text-anchor="middle">
      <text x="49" y="111">● Branch 1  ● Branch 2  ● Branch 3</text>
      <text x="135" y="111">● 1st Qtr  ● 2nd Qtr  ● 3rd Qtr  ● 4th Qtr</text>
      <text x="221" y="111">● Series 1  ● Series 2</text>
    </g>
  </svg>
  <div class="foot"><span class="foot__mark"><i></i>PLAYNOVA</span><span class="foot__rule"></span></div>
</section>

<!-- Icons feature slide -->
<section class="slide slide--small" style="left:612px;top:364px">
  <div class="icon-card" style="left:6px">
    <div class="icon-card__box"><svg width="18" height="26" viewBox="0 0 18 26" fill="none" stroke="var(--cyan)" stroke-width="1"><rect x="2" y="1" width="14" height="24" rx="2"/><rect x="5" y="4" width="8" height="7"/><circle cx="9" cy="18" r="3"/></svg></div>
    <div class="icon-card__title">Super duper title</div>
    <div class="icon-card__text">Cool description. Far far away, behind the word</div>
  </div>
  <div class="icon-card" style="left:72px">
    <div class="icon-card__box"><svg width="30" height="18" viewBox="0 0 30 18" fill="none" stroke="var(--cyan)" stroke-width="1"><rect x="1" y="3" width="28" height="12" rx="6"/><path d="M7 7v4M5 9h4"/><circle cx="21" cy="9" r="2.5"/></svg></div>
    <div class="icon-card__title">Super duper title</div>
    <div class="icon-card__text">Cool description. Far far away, behind the word</div>
  </div>
  <div class="icon-card" style="left:138px">
    <div class="icon-card__box"><svg width="20" height="28" viewBox="0 0 20 28" fill="none" stroke="var(--cyan)" stroke-width="1"><path d="M10 2a8 8 0 0 0-5 14v4h10v-4A8 8 0 0 0 10 2z"/><path d="M6 23h8M7 26h6"/></svg></div>
    <div class="icon-card__title">Super duper title</div>
    <div class="icon-card__text">Cool description. Far far away, behind the word</div>
  </div>
  <div class="icon-card" style="left:204px">
    <div class="icon-card__box"><svg width="26" height="26" viewBox="0 0 26 26" fill="none" stroke="var(--cyan)" stroke-width="1"><path d="M2 12L24 2 16 24 12 14z"/><path d="M12 14L24 2"/></svg></div>
    <div class="icon-card__title">Super duper title</div>
    <div class="icon-card__text">Cool description. Far far away, behind the word</div>
  </div>
  <div class="foot"><span class="foot__mark"><i></i>PLAYNOVA</span><span class="foot__rule"></span></div>
</section>

<!-- Scooter slide -->
<section class="slide slide--small" style="left:898px;top:364px">
  <div class="fill" role="img" aria-label="Watercolour illustration of a red scooter" style="left:6px;top:6px;width:126px;height:140px;background:radial-gradient(circle at 55% 45%,#d9534f 0,#b8453f 35%,#e9e9e9 70%)"></div>
  <div class="abs" style="left:148px;top:56px;width:106px;text-align:center">
    <div class="s-title" style="font-size:8px">Cool title</div>
    <p class="tiny" style="margin-top:4px;font-size:4.4px;line-height:5.6px">Far far away, behind the word hills, far from the busy towns, there live the quiet words. They rest by the river near the coast, beside a wide ocean.</p>
  </div>
  <div class="foot" style="left:158px"><span class="foot__mark"><i></i>PLAYNOVA</span><span class="foot__rule"></span></div>
</section>

<!-- Two-photo slide -->
<section class="slide slide--small" style="left:612px;top:531px">
  <div class="fill" role="img" aria-label="Photo of fresh strawberries" style="left:6px;top:6px;width:83px;height:140px;background:linear-gradient(160deg,#c8323a,#8e1c24 60%,#b22a32)"></div>
  <div class="fill" role="img" aria-label="Photo of green limes" style="left:94px;top:6px;width:170px;height:140px;background:radial-gradient(circle at 40% 40%,#cfd64a,#8bb02a 55%,#5b7d1e)"></div>
</section>

<!-- Three-image slide -->
<section class="slide slide--small" style="left:898px;top:531px">
  <div class="fill" role="img" aria-label="Watercolour of a green vintage car" style="left:6px;top:6px;width:86px;height:124px;background:linear-gradient(180deg,#7aa85a,#5b8a44 60%,#b9a98a)"></div>
  <div class="fill" role="img" aria-label="Watercolour of a blue vintage van" style="left:92px;top:6px;width:86px;height:124px;background:linear-gradient(180deg,#5b9ad0,#2e6aa8 60%,#a6b4c2)"></div>
  <div class="fill" role="img" aria-label="Watercolour of a red vintage van" style="left:178px;top:6px;width:86px;height:124px;background:linear-gradient(180deg,#d8a890,#c84a36 60%,#b49c84)"></div>
  <div class="overlay-title" style="left:6px;top:90px">Super title</div>
  <div class="overlay-text" style="left:6px;top:101px">Cool description. Far far away, behind the word hills.</div>
  <div class="overlay-title" style="left:92px;top:90px">Super title</div>
  <div class="overlay-text" style="left:92px;top:101px">Cool description. Far far away, behind the word hills.</div>
  <div class="overlay-title" style="left:178px;top:90px">Super title</div>
  <div class="overlay-text" style="left:178px;top:101px">Cool description. Far far away, behind the word hills.</div>
  <div class="foot"><span class="foot__mark"><i></i>PLAYNOVA</span><span class="foot__rule"></span></div>
</section>

<!-- Magnifier over the template -->
<div class="magnifier" style="left:586px;top:288px;width:104px;height:104px;border:3px solid #e8e8e8">
  <div class="fill" style="left:0;top:0;width:104px;height:30px;background:#3a3a3a"></div>
  <div class="abs" style="left:36px;top:56px">
    <div class="wordmark" style="gap:2px"><span class="wordmark__square" style="width:5px;height:5px"></span><span class="wordmark__name" style="font-size:8px">PLAYNOVA</span></div>
  </div>
  <div class="fill" style="left:92px;top:61px;width:12px;height:1px;background:var(--rule)"></div>
</div>

<!-- Text + image slide -->
<section class="slide slide--small" style="left:31px;top:697px;width:274px">
  <div class="fill" role="img" aria-label="Watercolour of a blue camper van" style="left:6px;top:6px;width:80px;height:140px;background:linear-gradient(180deg,#e6e2da,#3d6ab0 45%,#27457e 75%,#d8d4cc)"></div>
  <div class="abs" style="left:97px;top:16px;width:170px">
    <div class="s-title" style="font-size:8px">Awesome Title</div>
    <p class="tiny" style="margin-top:5px;font-size:4.4px;line-height:5.7px">Far away, beyond the tall hills, far from the busy towns, there live quiet words. They rest by the river near the coast of a wide ocean. A small stream flows past their homes and brings them news. It is a bright land where sentences grow. Even the loudest word stops to listen here. One day a short line of text decided to leave home for the wide world of grammar. Her friends asked her to stay, but the little line did not listen.</p>
  </div>
  <div class="foot" style="left:126px"><span class="foot__mark"><i></i>PLAYNOVA</span><span class="foot__rule"></span></div>
</section>

<!-- Icon sheet A -->
<section class="slide slide--small" style="left:322px;top:697px;width:275px">
  <div class="sheet-label" style="left:7px;top:5px;font-weight:700">Icons</div>
  <div class="sheet-label" style="left:7px;top:23px">Arrows</div>
  <div class="sheet-label" style="left:93px;top:23px">Basic</div>
  <div class="sheet-label" style="left:181px;top:23px">Basic elaboration</div>
  <svg class="abs" style="left:7px;top:32px" width="262" height="100" viewBox="0 0 262 100">
    <defs>
      <pattern id="icon-grid-a" width="7" height="8" patternUnits="userSpaceOnUse">
        <rect x="1.5" y="1.5" width="4" height="4" rx="1" fill="none" stroke="var(--cyan)" stroke-width=".5"/>
      </pattern>
    </defs>
    <rect x="0" y="0" width="84" height="96" fill="url(#icon-grid-a)"/>
    <rect x="86" y="0" width="86" height="88" fill="url(#icon-grid-a)"/>
    <rect x="174" y="0" width="88" height="100" fill="url(#icon-grid-a)"/>
  </svg>
  <div class="foot"><span class="foot__mark"><i></i>PLAYNOVA</span><span class="foot__rule"></span></div>
</section>

<!-- Icon sheet B -->
<section class="slide slide--small" style="left:612px;top:697px">
  <div class="sheet-label" style="left:6px;top:5px;font-weight:700">Icons</div>
  <div class="sheet-label" style="left:6px;top:23px">Ecommerce</div>
  <div class="sheet-label" style="left:93px;top:23px">Music</div>
  <div class="sheet-label" style="left:93px;top:61px">Weather</div>
  <svg class="abs" style="left:6px;top:32px" width="258" height="100" viewBox="0 0 258 100">
    <defs>
      <pattern id="icon-grid-b" width="7" height="8" patternUnits="userSpaceOnUse">
        <circle cx="3.5" cy="3.5" r="2.2" fill="none" stroke="var(--cyan)" stroke-width=".5"/>
      </pattern>
    </defs>
    <rect x="0" y="0" width="84" height="52" fill="url(#icon-grid-b)"/>
    <rect x="87" y="0" width="171" height="24" fill="url(#icon-grid-b)"/>
    <rect x="87" y="36" width="171" height="64" fill="url(#icon-grid-b)"/>
  </svg>
  <div class="foot"><span class="foot__mark"><i></i>PLAYNOVA</span><span class="foot__rule"></span></div>
</section>

<!-- Magnifier over icons -->
<div class="magnifier" style="left:739px;top:706px;width:112px;height:112px">
  <svg width="112" height="112" viewBox="0 0 112 112" fill="none" stroke="var(--cyan)" stroke-width="1.2" stroke-linecap="round">
    <path d="M37 31c0-6 4-9 7-9s7 3 7 9v6l2 3H35l2-3z"/><path d="M42 42a2 2 0 0 0 4 0"/>
    <circle cx="66" cy="30" r="8"/><path d="M60 24l12 12"/>
    <path d="M88 20l4 4-10 12-3-1z"/>
    <rect x="22" y="50" width="10" height="16"/><path d="M27 53v10M25 61l2 2 2-2"/>
    <path d="M44 54h4l5-4v16l-5-4h-4z"/><path d="M57 55l5 6M62 55l-5 6"/>
    <path d="M72 52v12"/><circle cx="70" cy="64" r="2"/><path d="M72 52l6 2v10"/><circle cx="76" cy="64" r="2"/>
    <path d="M90 52v12"/><circle cx="88" cy="64" r="2"/><path d="M90 52l4 3"/>
    <path d="M22 80h6l10 10h6M22 90h6l10-10h6"/><path d="M42 78l2 2-2 2M42 88l2 2-2 2"/>
    <circle cx="56" cy="85" r="8"/><rect x="53" y="82" width="6" height="6"/>
    <rect x="70" y="79" width="16" height="12"/><path d="M73 85h10"/>
  </svg>
</div>

<!-- Collage slide -->
<section class="slide slide--small" style="left:898px;top:697px">
  <div class="fill" role="img" aria-label="Photo of a rocky island reflected in still water" style="left:6px;top:6px;width:80px;height:140px;background:linear-gradient(180deg,#d2d6d8,#6d7476 50%,#c8ccce)"></div>
  <div class="fill" role="img" aria-label="Photo of a waterfall with a hiker and rainbow" style="left:95px;top:6px;width:123px;height:40px;background:linear-gradient(180deg,#8b8d88,#5a5f58)"></div>
  <div class="fill" role="img" aria-label="Photo of a calm blue sea" style="left:95px;top:50px;width:39px;height:48px;background:linear-gradient(180deg,#6aa4d0,#2c6aa0)"></div>
  <div class="fill" role="img" aria-label="Photo of a castle in a green valley" style="left:138px;top:50px;width:80px;height:48px;background:linear-gradient(180deg,#c8d2d8,#6d8a5a)"></div>
  <div class="fill" role="img" aria-label="Photo of feet resting on a grassy hilltop" style="left:95px;top:102px;width:39px;height:44px;background:linear-gradient(180deg,#7c9a54,#4e6a34)"></div>
  <div class="fill" role="img" aria-label="Photo of snowy mountains over a lake" style="left:138px;top:102px;width:126px;height:44px;background:linear-gradient(180deg,#e6ecf0,#8a9aa6 55%,#3a4e5e)"></div>
  <div class="fill" role="img" aria-label="Photo of waves on a dark sea" style="left:224px;top:6px;width:40px;height:92px;background:linear-gradient(180deg,#c2cdd4,#3f5c70 50%,#1f3444)"></div>
</section>

<!-- Feature copy -->
<div class="feature" style="left:31px">
  <h2 class="feature__head">Ultra easy to use</h2>
  <p class="feature__body" style="margin-top:34px">Based on:<br>. master slides<br>. image placeholders<br>. the color of your brand</p>
</div>
<div class="feature" style="left:420px">
  <h2 class="feature__head">Fresh and<br>straightforward</h2>
  <p class="feature__body" style="margin-top:34px">To keep your audience<br>focused on what matters</p>
</div>
<div class="feature" style="left:809px">
  <h2 class="feature__head">To all look good!</h2>
  <p class="feature__body" style="margin-top:34px">Contains +700 stylized extra<br>icons that you can resize<br>and change colors while<br>keeping its high quality</p>
</div>

</body>
</html>
```